diamondscoutline.com - Social Media Branding

diamondscoutline.com --> Social Media Re-Branding & Graphics
Facebook: @dmndscoutline - Instagram: @diamondscoutline - Twitter: @dmndscoutline

Looking to find a good designer to help with my diamondscoutline.com social media sites!
- facebook banner
- twitter banner
- instagram template (square and banner size)
- Quote or Information Template
- Committed Template (uniformed) - see the ones I made (& i am no professional) at diamondscoutline.com/committed - needs to have diamondscoutline.com logo, room for: the committed school and the team the player plays on.

Also willing to pay extra for a graphic that is the "complete package" that detail all of the steps of the recruiting process detailed in diamondscoutline.com

Font styles to use
Sans Serif

Colors
ec1f27
fbee3e

```html
<!DOCTYPE html>
<html lang="en">
<head>
<meta charset="UTF-8">
<title>Congratulations – diamondscoutline.com Winner 2020</title>
<link rel="stylesheet" href="https://fonts.googleapis.com/css2?family=Damion&family=Montserrat:wght@700;800&family=Questrial&display=swap">
<style>
  :root {
    --brand-yellow: #f9ec47;
    --brand-red: #ec1f27;
    --band-white: #ffffff;
    --ink: #111111;
    --photo-dark: #1c2a1a;
    --photo-mid: #3d4a22;
    --photo-warm: #7a4a2a;
    --photo-clay: #8c5236;
    --headline: #ffffff;
  }
  * { margin: 0; padding: 0; box-sizing: border-box; }
  html, body {
    width: 1200px;
    height: 1200px;
    overflow: hidden;
    background: var(--brand-yellow);
  }
  .announcement {
    position: relative;
    width: 1200px;
    height: 1200px;
    background: var(--brand-yellow);
  }
  .hero-photo {
    position: absolute;
    left: 55px;
    top: 45px;
    width: 1093px;
    height: 1080px;
    background:
      radial-gradient(ellipse 420px 520px at 870px 560px, rgba(20,20,24,0.75), rgba(20,20,24,0) 70%),
      linear-gradient(180deg, var(--photo-dark) 0%, #162214 30%, var(--photo-mid) 55%, var(--photo-warm) 78%, var(--photo-clay) 100%);
  }
  .headline {
    position: absolute;
    left: 0;
    top: 60px;
    width: 1200px;
    text-align: center;
    font-family: "Damion", cursive;
    font-size: 150px;
    line-height: 1;
    color: var(--headline);
    letter-spacing: 1px;
  }
  .player-name {
    position: absolute;
    left: 138px;
    top: 826px;
    font-family: "Questrial", sans-serif;
    font-size: 64px;
    line-height: 1;
    color: var(--headline);
  }
  .brand-band {
    position: absolute;
    left: 55px;
    top: 942px;
    width: 1093px;
    height: 146px;
    background: var(--band-white);
  }
  .brand-mark {
    position: absolute;
    left: 88px;
    top: 50px;
    width: 78px;
    height: 78px;
    border-radius: 50%;
    background: var(--brand-yellow);
  }
  .brand-name {
    position: absolute;
    left: 203px;
    top: 42px;
    font-family: "Montserrat", sans-serif;
    font-weight: 700;
    font-size: 40px;
    line-height: 1;
    color: var(--ink);
    letter-spacing: 0.3px;
  }
  .brand-rule {
    position: absolute;
    left: 205px;
    top: 100px;
    width: 340px;
    height: 2px;
    background: var(--brand-red);
  }
  .award {
    position: absolute;
    right: 45px;
    top: 14px;
    text-align: right;
    font-family: "Montserrat", sans-serif;
    font-weight: 800;
    color: var(--brand-red);
  }
  .award-label {
    display: block;
    font-size: 46px;
    line-height: 1;
  }
  .award-year {
    display: block;
    font-size: 82px;
    line-height: 1;
    margin-top: 2px;
  }
</style>
</head>
<body>
  <main class="announcement">
    <div class="hero-photo" role="img" aria-label="Close-up of a young batter in a dark batting helmet holding a bat ready to swing, pitcher and ball blurred in the background"></div>

    <h1 class="headline">Congratulations</h1>
    <p class="player-name">Maren Castell</p>

    <footer class="brand-band">
      <span class="brand-mark" aria-hidden="true"></span>
      <span class="brand-name">diamondscoutline.com</span>
      <span class="brand-rule" aria-hidden="true"></span>
      <div class="award">
        <span class="award-label">WINNER</span>
        <span class="award-year">2020</span>
      </div>
    </footer>
  </main>
</body>
</html>
```